Website Refresh Needed - Large Couples Therapy Group

We are a large couples counselling group in Australia, and we have some key pages of our website that need refreshing, as it's a few years old now.
Similar colour palette as currently, and the same colours as the logo. No new logo required.
Total of 7 new (updated) page templates designs are needed:
1. HOME: https://www.velmoraclinic.com.au/
2: CONTACT US: https://www.velmoraclinic.com.au/contact/
3: RC CITY PAGE: https://www.velmoraclinic.com.au/city/sydney/
4: ST CITY PAGE: https://www.velmoraclinic.com.au/our-counselling/sex-therapy/sex-therapy-sydney/
5: ALL BLOGS: https://www.velmoraclinic.com.au/blog/
6: BLOG: https://www.velmoraclinic.com.au/sexual-desires-in-men-and-women-what-are-the-real-differences/
7: MAIN STANDARD PAGE: https://www.velmoraclinic.com.au/our-counselling/couples-relationship-counselling/

Target Market(s)

couples who are going through a crisis in their relationship or marriage.

Number of Pages Required

5+ page

Colors
86cfc6
b8a6cd
cfdfed

Requirements
Must have
• Calm, reassuring colours. People are stressed and need to know we can help.
Should not have
• No bright oranges or yellows.

```html
<!DOCTYPE html>
<html lang="en">
<head>
<meta charset="utf-8">
<title>Velmora Clinic – Relationship & Marriage Counselling</title>
<link href="https://fonts.googleapis.com/css2?family=Arimo:wght@400;700&family=Raleway:wght@300;400&display=swap" rel="stylesheet">
<style>
:root{
  --teal:#2a9aa8;
  --teal-dark:#1f8592;
  --mint:#86cfc6;
  --lav:#b8a6cd;
  --sky:#cfdfed;
  --ink:#1e1e1e;
  --text:#333;
  --pale:#f2f8fb;
  --lav-pale:#f4f0f9;
  --foot:#eaf2f8;
}
*{margin:0;padding:0;box-sizing:border-box}
html,body{width:1200px;height:4133px;overflow:hidden}
body{font-family:"Arimo",Arial,sans-serif;color:var(--text);background:#fff;position:relative}
.abs{position:absolute}
a{color:inherit}
section,header,nav,footer{position:absolute;left:0;width:1200px}
.topbar{top:0;height:38px;background:linear-gradient(90deg,#2a9aa8,#35a7b3)}
.social{display:flex;gap:20px}
.social i{display:block;width:18px;height:18px;border:2px solid currentColor;border-radius:50%}
.topbar .social{left:134px;top:10px;color:#fff}
.topbar .enquire{left:558px;top:10px;font-size:14px;color:#fff;text-decoration:underline}
.topbar .appt{left:914px;top:6px;width:196px;height:26px;background:#fff;border-radius:13px;color:var(--teal);font-size:14px;text-align:center;line-height:26px}
.site-header{top:38px;height:103px;background:#fff}
.brand{display:flex;align-items:center;gap:12px}
.brand .dot{width:46px;height:46px;border-radius:50%;background:var(--teal)}
.brand .name{font-family:"Raleway",sans-serif;font-weight:400;font-size:34px;color:var(--teal)}
.site-header .brand{left:45px;top:26px}
.contact-item{display:flex;align-items:center;gap:10px;top:32px;font-size:14px;color:var(--ink);line-height:18px}
.contact-item .ico{width:50px;height:50px;border-radius:50%;background:var(--mint);display:flex;align-items:center;justify-content:center}
.contact-item b{display:block;font-size:15px}
.main-nav{top:141px;height:52px;background:var(--sky)}
.main-nav .burger{left:67px;top:17px}
.main-nav ul{list-style:none;position:absolute;top:18px;left:0;font-size:15px;color:var(--ink)}
.main-nav li{position:absolute;white-space:nowrap}
.main-nav li.on{color:var(--teal)}
.search-box{left:922px;top:12px;width:204px;height:26px;background:#fff;border:1px solid #c9d3dc;border-radius:13px;font-size:12px;color:#999;padding:6px 14px}
.search-box .go{position:absolute;right:-1px;top:-1px;width:42px;height:26px;background:var(--lav);border-radius:13px;display:flex;align-items:center;justify-content:center}
.hero{top:193px;height:540px;background:linear-gradient(90deg,#8e9aa3 0%,#c8ccd0 40%,#e3e8ec 70%,#eef2f5 100%)}
.hero .photo{left:0;top:0;width:620px;height:540px;background:linear-gradient(100deg,#7b858c,#b7bfc5 70%,rgba(220,226,230,0))}
.hero h1{left:510px;top:300px;width:560px;text-align:center;font-size:42px;line-height:48px;font-weight:700;color:var(--mint);letter-spacing:.5px}
.hero .mark{left:709px;top:130px;width:110px;height:110px;border-radius:50%;background:var(--teal);opacity:.85}
.dots{display:flex;gap:9px}
.dots i{width:6px;height:6px;border-radius:50%;background:var(--mint);opacity:.6}
.dots i:first-child{opacity:1}
.hero .dots{left:582px;top:523px}
.finder{top:733px;height:133px;background:var(--sky)}
.finder h2{left:173px;top:14px;font-size:27px;font-weight:700;color:#3a4a55}
.finder form{left:173px;top:55px;width:847px;height:51px;display:flex;background:#fff;border-radius:26px;box-shadow:0 2px 6px rgba(0,0,0,.12);overflow:hidden;font-size:14px;color:#8a8f95}
.finder .fld{height:51px;display:flex;align-items:center;justify-content:space-between;padding:0 16px;border-right:1px solid #dde3e8}
.finder .btn{flex:1;background:var(--lav);color:#fff;display:flex;align-items:center;justify-content:center;font-size:15px}
.eyebrow{font-size:18px;font-weight:700;color:var(--ink);letter-spacing:.3px}
.lead{font-family:"Raleway",sans-serif;font-weight:300;font-size:32px;line-height:38px;color:var(--mint)}
.copy{font-size:13.5px;line-height:19px;color:#333}
.copy p{margin-bottom:19px}
.pill{display:inline-block;height:34px;line-height:34px;padding:0 16px;border-radius:17px;background:var(--lav);color:#fff;font-size:14px}
.pill.mint{background:var(--mint)}
.about{top:866px;height:481px}
.photo{border-radius:2px}
.about .photo{left:784px;top:85px;width:326px;height:326px;background:linear-gradient(150deg,#c9b7a3,#8f8a88 60%,#5f6b74)}
.types{top:1347px;height:642px;background:var(--pale);text-align:center}
.types .eyebrow{top:30px;width:1200px;left:0}
.types .lead{top:68px;width:1200px;left:0}
.card{top:180px;width:268px;text-align:center}
.card .circ{width:218px;height:218px;border-radius:50%;margin:0 auto;display:flex;align-items:center;justify-content:center}
.card h3{font-family:"Raleway",sans-serif;font-weight:400;font-size:27px;line-height:32px;color:var(--mint);margin-top:30px}
.card p{font-size:14px;font-weight:700;line-height:19px;color:#333;margin-top:19px;padding:0 20px}
.issues{top:1989px;height:631px}
.issues .eyebrow{top:58px;width:1200px;left:0;text-align:center}
.issues .lead{top:94px;width:1200px;left:0;text-align:center}
.issues ul{list-style:none;font-size:20px;color:#444}
.issues li{position:relative;padding-left:34px;height:45px;line-height:24px}
.issues li::before{content:"";position:absolute;left:0;top:6px;width:13px;height:13px;border-radius:50% 50% 50% 0;transform:rotate(-45deg);background:var(--lav)}
.issues li:nth-child(even)::before{background:var(--mint)}
.issues .figure{left:385px;top:224px;width:385px;height:407px;background:radial-gradient(ellipse at 50% 45%,#b7b9bc 0%,#d6d8da 45%,#ffffff 80%)}
.approach{top:2620px;height:521px;background:var(--lav-pale)}
.approach .photo{left:674px;top:102px;width:473px;height:363px;background:linear-gradient(120deg,#cfc3b6,#a79f98 50%,#6a7880)}
.blogs{top:3141px;height:609px}
.thumb{background:linear-gradient(135deg,#9a8f86,#5d6870)}
.faq{left:603px;width:520px}
.faq .item{position:absolute;left:0;display:flex;gap:20px}
.faq .thumb{width:108px;height:109px;flex:none}
.faq h4{font-weight:400;font-size:20px;line-height:25px;color:#3a4a55;text-decoration:underline;margin-top:2px}
.faq .more{font-size:14px;color:var(--mint);margin-top:18px}
.site-footer{top:3750px;height:329px;background:var(--foot)}
.site-footer h5{font-size:13px;font-weight:400;color:#444;letter-spacing:.3px}
.site-footer ul{list-style:none;font-size:13px;line-height:26px;color:#444;margin-top:14px}
.news input{display:block;width:233px;height:34px;border:1px solid #b7c4ce;border-radius:17px;background:#fff;padding:0 18px;font-size:12px;font-family:inherit;color:#999;margin-top:12px}
.up{left:1061px;top:234px;width:56px;height:56px;border-radius:50%;background:var(--teal);display:flex;align-items:center;justify-content:center}
.legal{top:4079px;height:54px;background:var(--teal);color:#fff;font-size:13px;padding:20px 96px}
</style>
</head>
<body>

<div class="topbar abs" style="position:absolute;left:0;width:1200px">
  <div class="social abs"><i></i><i></i><i></i><i></i></div>
  <a class="enquire abs" href="#">Enquire About Our Associate Program</a>
  <a class="appt abs" href="#" style="text-decoration:none">Request an appointment</a>
</div>

<header class="site-header">
  <div class="brand abs"><span class="dot"></span><span class="name">Velmora Clinic</span></div>
  <div class="contact-item abs" style="left:433px">
    <span class="ico"><svg width="22" height="22" viewBox="0 0 24 24"><path fill="#fff" d="M6.6 10.8a15 15 0 0 0 6.6 6.6l2.2-2.2c.3-.3.7-.4 1-.2 1.1.4 2.3.6 3.6.6.6 0 1 .4 1 1V20c0 .6-.4 1-1 1A17 17 0 0 1 3 4c0-.6.4-1 1-1h3.5c.6 0 1 .4 1 1 0 1.3.2 2.5.6 3.6.1.3 0 .7-.2 1z"/></svg></span>
    <span><b>Phone</b>1300 482 917</span>
  </div>
  <div class="contact-item abs" style="left:642px">
    <span class="ico"><svg width="24" height="18" viewBox="0 0 24 18"><rect x="1" y="1" width="22" height="16" rx="2" fill="#fff"/><path d="M2 2l10 8 10-8" stroke="#86cfc6" stroke-width="2" fill="none"/></svg></span>
    <span><b>Email</b>hello@velmoraclinic.com</span>
  </div>
  <div class="contact-item abs" style="left:884px">
    <span class="ico"><svg width="18" height="24" viewBox="0 0 18 24"><path fill="#fff" d="M9 0a9 9 0 0 0-9 9c0 7 9 15 9 15s9-8 9-15a9 9 0 0 0-9-9zm0 12a3 3 0 1 1 0-6 3 3 0 0 1 0 6z"/></svg></span>
    <span><b>Location</b>house- 3/4, Road, Place</span>
  </div>
</header>

<nav class="main-nav">
  <svg class="burger abs" width="28" height="20" viewBox="0 0 28 20"><path d="M0 2h28M0 10h28M0 18h28" stroke="#2a9aa8" stroke-width="2.5"/></svg>
  <ul>
    <li class="on" style="left:131px">HOME</li>
    <li style="left:228px">ABOUT</li>
    <li style="left:332px">COUNSELLING TYPE</li>
    <li style="left:542px">LOCATIONS</li>
    <li style="left:683px">CONTACT US</li>
  </ul>
  <div class="search-box abs">search...
    <span class="go"><svg width="12" height="12" viewBox="0 0 12 12"><circle cx="5" cy="5" r="3.5" stroke="#fff" stroke-width="1.6" fill="none"/><path d="M7.5 7.5L11 11" stroke="#fff" stroke-width="1.6"/></svg></span>
  </div>
</nav>

<section class="hero">
  <div class="photo abs" role="img" aria-label="Smiling couple embracing by the water"></div>
  <div class="mark abs"></div>
  <h1 class="abs">EXPERT RELATIONSHIP &amp;<br>MARRIAGE COUNSELLING</h1>
  <div class="dots abs"><i></i><i></i><i></i></div>
</section>

<section class="finder">
  <h2 class="abs">Search our Therapists Near You</h2>
  <form class="abs">
    <div class="fld" style="width:226px">Type Of Counselling <svg width="14" height="8"><path d="M1 1l6 6 6-6" stroke="#999" fill="none"/></svg></div>
    <div class="fld" style="width:228px"><span><svg width="10" height="13" viewBox="0 0 18 24" style="margin-right:8px"><path fill="none" stroke="#999" stroke-width="2" d="M9 1a8 8 0 0 0-8 8c0 6 8 14 8 14s8-8 8-14a8 8 0 0 0-8-8z"/></svg>Location</span><svg width="14" height="8"><path d="M1 1l6 6 6-6" stroke="#999" fill="none"/></svg></div>
    <div class="fld" style="width:145px"><span><svg width="14" height="13" style="margin-right:8px"><rect x="1" y="2" width="12" height="10" stroke="#999" fill="none"/></svg>Dec 20</span><svg width="14" height="8"><path d="M1 1l6 6 6-6" stroke="#999" fill="none"/></svg></div>
    <div class="fld" style="width:146px">Postal Code</div>
    <div class="btn">Search</div>
  </form>
</section>

<section class="about">
  <div class="eyebrow abs" style="left:88px;top:72px">ABOUT US</div>
  <h2 class="lead abs" style="left:88px;top:112px">We Specialise in Relationship<br>&amp; Marriage Counselling</h2>
  <div class="copy abs" style="left:88px;top:213px;width:516px">
    <p>Welcome to the Velmora Clinic....</p>
    <p>You've come to the right place if you value your relationship, (along with being true to yourself) and would like help with how to repair the inevitable difficulties that come up in most relationships, and build a stronger more authentic connection.</p>
    <p>None of us, when we fall in love, imagine how difficult our relationship is going to be at times. We always hope for the best, of them.</p>
  </div>
  <a class="pill abs" href="#" style="left:88px;top:411px;text-decoration:none">Read More</a>
  <div class="photo abs" role="img" aria-label="Portrait of a smiling counsellor with blonde hair"></div>
</section>

<section class="types">
  <div class="eyebrow abs">COUNSELLING TYPES</div>
  <h2 class="lead abs">Helping You to<br>Create Loving Relationship</h2>
  <div class="card abs" style="left:62px">
    <div class="circ" role="img" aria-label="Couple sitting together on a sofa" style="background:linear-gradient(135deg,#d8d3cc,#8f979d)"></div>
    <h3>Relationship<br>Counselling</h3>
    <p>Do you need help with:<br>Communication, recovering from an affair, loss of intimacy and love or power battles?</p>
  </div>
  <div class="card abs" style="left:330px">
    <div class="circ" role="img" aria-label="Couple lying among rose petals" style="background:linear-gradient(135deg,#e9e4e2,#b9a7a2)"></div>
    <h3>Sex Therapy<br>Counselling</h3>
    <p>Do you need help with:<br>Low sexual drive, erectile difficulties, premature ejaculation, differing libidos or porn addiction?</p>
  </div>
  <div class="card abs" style="left:599px">
    <div class="circ" role="img" aria-label="Stressed man holding his head" style="background:linear-gradient(135deg,#6f7f86,#3f4d55);border:3px solid var(--mint)"><span style="color:#fff;font-size:14px;text-decoration:underline">Learn More</span></div>
    <h3>Anger<br>Management</h3>
    <p>Do you need help with:<br>Managing irrational outbursts, while learning to express your anger in healthy ways?</p>
  </div>
  <div class="card abs" style="left:867px">
    <div class="circ" role="img" aria-label="Couple standing apart with arms crossed" style="background:linear-gradient(135deg,#e6e3df,#a29a92)"></div>
    <h3>Narcissism<br>Counselling</h3>
    <p>Do you need help with:<br>Managing narcissistic, superior, entitled, arrogant behaviour or lack of empathy?</p>
  </div>
</section>

<section class="issues">
  <div class="eyebrow abs">OUR RELATIONSHIP THERAPISTS</div>
  <h2 class="lead abs">Can help with the following common<br>relationship issues, and more:</h2>
  <div class="figure abs" role="img" aria-label="Couple standing back to back in soft grey tones"></div>
  <ul class="abs" style="left:88px;top:278px">
    <li>Affairs</li><li>Controlling behaviour</li><li>Verbal abuse</li><li>Imbalance of power</li><li>Lack of intimacy</li><li>Poor communication</li><li>Loss of love</li>
  </ul>
  <ul class="abs" style="left:781px;top:278px;width:360px">
    <li>Relationship neglect</li><li>Sexual problems</li><li>Problems from childhood</li><li style="height:70px">Problems with parenting<br>your children</li><li>Step children and in-laws</li><li>All forms of family problems</li><li>Anger management problems</li>
  </ul>
</section>

<section class="approach">
  <div class="eyebrow abs" style="left:88px;top:78px">VELMORA CLINIC</div>
  <h2 class="lead abs" style="left:88px;top:112px">Our Marriage Counselling<br>Approach</h2>
  <div class="copy abs" style="left:88px;top:224px;width:505px">
    <p>It is very important to us that we take a very positive approach to relationship counselling. From your very first session, we will take the time to fully understand each of your individual perspectives, without bias, and get to the very root of the issues that are affecting your relationship.</p>
    <p>Once we have a clear understanding of what's been going on, we will compassionately guide you and your partner beyond the dynamics that have been causing you problems.</p>
  </div>
  <a class="pill abs" href="#" style="left:88px;top:424px;text-decoration:none">Read More</a>
  <a class="pill mint abs" href="#" style="left:210px;top:424px;text-decoration:none">View Locations</a>
  <div class="photo abs" role="img" aria-label="Couple in a counselling session with coffee cups on the table"></div>
</section>

<section class="blogs">
  <h2 class="lead abs" style="left:106px;top:46px">Our Latest Blogs</h2>
  <div class="thumb abs" role="img" aria-label="Worried couple sitting on a couch" style="left:109px;top:120px;width:382px;height:261px"></div>
  <h3 class="abs" style="left:115px;top:402px;width:380px;font-weight:400;font-size:20px;line-height:25px;color:var(--mint)">Is Your Pursuit of Success Sabotaging Your Relationships That Matter Most?</h3>
  <p class="copy abs" style="left:115px;top:465px;width:380px">Many people find that their ways of communicating with each other hamper them from having a happy healthy relationship.</p>
  <div class="dots abs" style="left:281px;top:545px"><i></i><i></i><i></i></div>

  <div class="eyebrow abs" style="left:602px;top:77px;font-size:16px">FAQ's</div>
  <div class="faq abs" style="top:120px">
    <div class="item" style="top:0"><div class="thumb" role="img" aria-label="Woman looking down thoughtfully"></div><div><h4>Is Your Pursuit of Success Sabotaging Your Relationships That Matter Most?</h4><div class="more">Read More</div></div></div>
    <div class="item" style="top:125px"><div class="thumb" role="img" aria-label="Two people holding hands"></div><div><h4>Have You Lost Yourself in relationship? recover from an affair</h4><div class="more">Read More</div></div></div>
    <div class="item" style="top:249px"><div class="thumb" role="img" aria-label="Couple in conversation"></div><div><h4>Is Your Pursuit of Success Sabotaging Your Relationships That Matter Most?</h4><div class="more">Read More</div></div></div>
  </div>
  <a class="abs" href="#" style="left:982px;top:506px;font-size:14px;color:var(--mint)">View All Questions</a>
</section>

<footer class="site-footer">
  <div class="brand abs" style="left:88px;top:82px"><span class="dot"></span><span class="name">Velmora Clinic</span></div>
  <div class="social abs" style="left:96px;top:190px;color:#8a949b;gap:26px"><i></i><i></i><i></i><i></i></div>
  <div class="abs" style="left:518px;top:96px"><h5>MENUS</h5><ul><li>Home</li><li>About Us</li><li>Counselling</li><li>Our Blogs</li><li>Sex Theraphy</li><li>Contact Us</li></ul></div>
  <div class="abs" style="left:672px;top:96px"><h5>USEFUL LINKS</h5><ul><li>Terms&amp; condition</li><li>Privacy policy</li><li>Members Log In</li><li>Copyright</li></ul></div>
  <div class="news abs" style="left:842px;top:96px"><h5>JOIN OUR NEWSLETTER</h5><input type="text" value="Enter your email address" readonly><span class="pill" style="height:28px;line-height:28px;font-size:13px;margin-top:12px">Subscribe</span></div>
  <div class="up abs"><svg width="26" height="16" viewBox="0 0 26 16"><path d="M2 14L13 3l11 11" stroke="#fff" stroke-width="4" fill="none"/></svg></div>
</footer>

<div class="legal abs" style="position:absolute;left:0;width:1200px">© 2020 Velmora Clinic. All rights reserved.</div>

</body>
</html>
```